I am a company selling interior designing materials

HI, I am selling interior design materials and require a namecard which is more outstanding while following a certain details placement as attached.

My clients are mainly interior designers so it has to attract their attention rather than feeling that its "just another namecard". I am selling wallcoverings, fabrics, acoustics and carpets.

Target Market(s)

interior designers designing hotels, commerical offices.

Contact Information for Business Card

As per attached.
Please change address to 47 Jalan 16 Tembusu #05-02 Velmora Tower Singapore 417263

Font styles to use
Other font styles liked:
• calibri

Requirements
Must have
• (1) company logo on top in the middle. Placement of contac details to be the same
• (2) company color is blue/green cymk 75/8/42/0
• (3) "KDT" logo to be prominent
• (4) You may change the logo but there should be a "swirl" surrounding the word KDT like current logo. The swirl pattern does not need to follow current logo and you may propose.
Should not have
• (1) there should not be any designs above "KDT" logo
• (2) no sharp triangles or angles

```html
<!DOCTYPE html>
<html lang="en">
<head>
<meta charset="utf-8">
<title>KDT Business Card</title>
<link href="https://fonts.googleapis.com/css2?family=Nunito+Sans:wght@400;600;700;800;900&display=swap" rel="stylesheet">
<style>
  :root {
    --teal: #1faaa4;
    --teal-deep: #168f8a;
    --charcoal: #3a3a3c;
    --ink: #2b2b2d;
    --white: #ffffff;
    --grey: #8a8a8c;
    --stage: #2a2d32;
  }
  * { margin: 0; padding: 0; box-sizing: border-box; }
  html, body {
    width: 1200px;
    height: 1032px;
    overflow: hidden;
    background: var(--stage);
    font-family: "Nunito Sans", Calibri, sans-serif;
  }
  .card {
    position: absolute;
    width: 560px;
    height: 320px;
    border-radius: 28px;
    overflow: hidden;
  }

  /* Contact side */
  .card-contact { left: 580px; top: 110px; background: var(--white); }
  .card-contact .card-shape { position: absolute; inset: 0; }
  .brand {
    position: absolute;
    left: 200px;
    top: 22px;
    width: 320px;
    text-align: center;
  }
  .brand-mark {
    display: flex;
    align-items: center;
    justify-content: center;
    gap: 10px;
  }
  .brand-dot {
    width: 16px; height: 16px;
    border-radius: 50%;
    background: var(--teal);
  }
  .brand-name {
    font-weight: 900;
    font-size: 44px;
    line-height: 1;
    color: var(--ink);
    letter-spacing: 1px;
  }
  .company-name {
    margin-top: 8px;
    font-weight: 800;
    font-size: 14px;
    color: var(--ink);
  }
  .person {
    position: absolute;
    left: 250px;
    top: 118px;
  }
  .person-name {
    font-weight: 700;
    font-size: 24px;
    color: var(--teal);
  }
  .person-mobile {
    font-size: 14px;
    color: var(--grey);
    margin-top: 2px;
  }
  .address {
    position: absolute;
    left: 22px;
    top: 168px;
    color: var(--white);
    font-size: 13px;
    line-height: 1.45;
  }
  .address-label {
    color: var(--teal);
    font-weight: 700;
  }
  .contact-lines {
    position: absolute;
    right: 26px;
    bottom: 20px;
    text-align: right;
    color: var(--white);
    font-size: 15px;
    line-height: 1.45;
  }
  .contact-phone { font-weight: 700; font-size: 16px; }

  /* Brand side */
  .card-brand {
    left: 60px;
    top: 560px;
    background: linear-gradient(135deg, var(--teal) 0%, var(--teal-deep) 100%);
  }
  .card-brand .brand-mark {
    position: absolute;
    left: 0; right: 0;
    top: 82px;
    gap: 18px;
  }
  .card-brand .brand-dot { width: 26px; height: 26px; background: var(--white); }
  .card-brand .brand-name {
    color: var(--white);
    font-size: 108px;
    letter-spacing: 2px;
  }
  .services {
    position: absolute;
    left: 30px;
    bottom: 26px;
    color: var(--white);
    font-weight: 700;
    font-size: 17px;
    letter-spacing: 0.3px;
  }
</style>
</head>
<body>

  <section class="card card-contact">
    <svg class="card-shape" width="560" height="320" viewBox="0 0 560 320" aria-hidden="true">
      <path d="M0,40 C140,170 340,232 560,232 L560,250 C340,252 140,200 0,72 Z" fill="var(--teal)"/>
      <path d="M0,72 C140,200 340,252 560,250 L560,320 L0,320 Z" fill="var(--charcoal)"/>
    </svg>

    <div class="brand">
      <div class="brand-mark">
        <span class="brand-name">KDT</span>
        <span class="brand-dot"></span>
      </div>
      <p class="company-name">Kendaltree Interior Furnishings Pte Ltd</p>
    </div>

    <div class="person">
      <p class="person-name">Mirelle TAN</p>
      <p class="person-mobile">(65) 9172 5530</p>
    </div>

    <div class="address">
      <p class="address-label">Kendaltree</p>
      <p>47 Jalan 16 Tembusu #05-02</p>
      <p>Velmora Tower Singapore 417263</p>
    </div>

    <div class="contact-lines">
      <p class="contact-phone">(65) 6284 7105</p>
      <p>mirelle@kdtfurnishings.com</p>
    </div>
  </section>

  <section class="card card-brand">
    <div class="brand-mark">
      <span class="brand-name">KDT</span>
      <span class="brand-dot"></span>
    </div>
    <p class="services">Wallcoverings &bull; Acoustic &bull; Fabrics &bull; Carpet</p>
  </section>

</body>
</html>
```